Stationery Design Project

We are interested in A4 paper letterheads, envelopes, maybe A4 folders where we can put the patients' results in and businesscards. No information will be given out for the time being.
We would like to see mainly shades of white.. please refer to
http://en.huevaultix.org/wiki/Category:Shades_of_white
anti-flash white, splashed white,ghost white, ivory, snow and white smoke or even light grey
we are interested mainly on the silver design but we welcome the other colors as well. Since its about a gynecologist please avoid dark colors, instead use shades of beige, light grey and white

```html
<!DOCTYPE html>
<html lang="en">
<head>
<meta charset="utf-8">
<title>Lunaria Stationery Set</title>
<link rel="stylesheet" href="https://fonts.googleapis.com/css2?family=Arimo:wght@400;700&family=Montserrat:wght@400;500;600&display=swap">
<style>
  :root {
    --bg: #d6d6d8;
    --paper: #ffffff;
    --blush: #f7dfe8;
    --blush-deep: #e8c7d4;
    --silver: #a9a9ae;
    --silver-dark: #7d7d83;
    --ink: #2e2e32;
    --ink-soft: #6a6a70;
  }
  * { margin: 0; padding: 0; box-sizing: border-box; }
  html, body { width: 1200px; height: 927px; overflow: hidden; background: var(--bg); }
  .canvas { position: relative; width: 1200px; height: 927px; overflow: hidden; background: var(--bg); font-family: "Montserrat", sans-serif; color: var(--ink); }
  .defs { position: absolute; width: 0; height: 0; }

  .piece { position: absolute; background: var(--paper); box-shadow: 0 2px 6px rgba(0,0,0,0.12); overflow: hidden; }
  .wave { position: absolute; left: 0; top: 0; width: 100%; display: block; }

  .brand { position: absolute; display: flex; align-items: center; gap: 6px; font-family: "Montserrat", sans-serif; font-weight: 500; color: var(--silver-dark); letter-spacing: 0.06em; }
  .brand-dot { display: inline-block; border-radius: 50%; border: 1.5px solid var(--silver); }

  /* Folder */
  .folder { left: 40px; top: 216px; width: 350px; height: 495px; background: linear-gradient(100deg, var(--blush-deep) 0%, var(--blush) 55%, #fbeef3 100%); }
  .folder .brand { right: 28px; bottom: 48px; font-size: 20px; }
  .folder .brand-dot { width: 14px; height: 14px; }
  .folder-url { position: absolute; left: 24px; bottom: 14px; font-size: 6px; font-weight: 600; color: var(--ink-soft); }

  /* Letterhead */
  .letterhead { left: 420px; top: 216px; width: 350px; height: 495px; }
  .letterhead .wave { height: 80px; }
  .letterhead .brand { left: 18px; top: 16px; font-size: 12px; }
  .letterhead .brand-dot { width: 9px; height: 9px; }
  .letter { position: absolute; left: 24px; right: 24px; top: 112px; font-family: "Arimo", sans-serif; font-size: 5.6px; line-height: 1.55; color: var(--ink); }
  .letter-date { margin-bottom: 9px; }
  .letter-recipient { margin-bottom: 9px; }
  .letter p { margin-bottom: 6px; text-align: justify; }

  .contact-footer { position: absolute; display: flex; align-items: flex-start; font-size: 4.8px; line-height: 1.6; color: var(--ink-soft); }
  .contact-item { display: flex; align-items: center; gap: 3px; }
  .icon { width: 5px; height: 5px; flex: none; }
  .letterhead .contact-footer { left: 24px; right: 24px; bottom: 16px; gap: 36px; }

  /* Business card */
  .card { left: 800px; top: 216px; width: 360px; height: 206px; }
  .card .wave { height: 70px; }
  .card .brand { left: 26px; top: 86px; font-size: 17px; }
  .card .brand-dot { width: 12px; height: 12px; }
  .card-person { position: absolute; left: 196px; top: 76px; }
  .card-name { font-size: 9px; font-weight: 600; letter-spacing: 0.08em; }
  .card-title { font-size: 5.5px; color: var(--ink-soft); margin-top: 2px; }
  .card-address { position: absolute; left: 26px; bottom: 20px; font-size: 6.5px; line-height: 1.6; color: var(--ink-soft); }
  .card-contacts { position: absolute; left: 196px; top: 118px; font-size: 6.5px; line-height: 1.6; color: var(--ink-soft); }
  .card-contacts .icon { width: 6px; height: 6px; }

  /* Envelope */
  .envelope { left: 800px; top: 531px; width: 360px; height: 180px; }
  .envelope .wave { height: 62px; }
  .envelope .brand { left: 16px; top: 14px; font-size: 12px; }
  .envelope .brand-dot { width: 9px; height: 9px; }
  .envelope .contact-footer { left: 16px; right: 16px; bottom: 14px; gap: 30px; font-size: 4.4px; }
</style>
</head>
<body>
<main class="canvas">
  <svg class="defs" aria-hidden="true">
    <defs>
      <linearGradient id="silver-line" x1="0" x2="1" y1="0" y2="0">
        <stop offset="0" stop-color="#e4e4e6"/>
        <stop offset="0.35" stop-color="#9c9ca2"/>
        <stop offset="0.65" stop-color="#d8d8dc"/>
        <stop offset="1" stop-color="#8e8e94"/>
      </linearGradient>
      <linearGradient id="blush-band" x1="0" x2="1" y1="0" y2="0">
        <stop offset="0" stop-color="#f3d6e1"/>
        <stop offset="1" stop-color="#fae7ee"/>
      </linearGradient>
    </defs>
  </svg>

  <section class="piece folder" aria-label="Presentation folder">
    <div class="brand"><span class="brand-dot"></span>Lunaria</div>
    <div class="folder-url">www.lunaria-clinic.com</div>
  </section>

  <section class="piece letterhead" aria-label="Letterhead">
    <svg class="wave" viewBox="0 0 100 30" preserveAspectRatio="none" aria-hidden="true">
      <path d="M0,0 H100 V6 C80,6 66,24 38,22 C22,21 9,15 0,13 Z" fill="url(#blush-band)"/>
      <path d="M0,13 C9,15 22,21 38,22 C66,24 80,6 100,6" fill="none" stroke="url(#silver-line)" stroke-width="1.4"/>
    </svg>
    <div class="brand"><span class="brand-dot"></span>Lunaria</div>
    <div class="letter">
      <div class="letter-date">Bandung, 9 Maret 2012</div>
      <div class="letter-recipient">
        Kepada Yth.<br>
        Mr. Adrian Vale<br>
        12 Jalan Melati<br>
        Gedung Putih Lantai 3<br>
        Kebayoran Baru 118<br>
        Jakarta Selatan
      </div>
      <p>Dengan hormat,</p>
      <p>We are pleased to confirm your next consultation at our clinic. Please arrive fifteen minutes early and bring any previous results, referral letters and a list of current medication so our team can prepare your visit carefully.</p>
      <p>All results are stored securely and shared only with you. If you wish to change the date, contact our front desk by phone or email at least one day ahead.</p>
      <p>Thank you for your trust. We look forward to welcoming you.</p>
    </div>
    <div class="contact-footer">
      <div>21 Ivory Lane<br>PO Box 415<br>Snowfield, NV 89010</div>
      <div>
        <div class="contact-item"><svg class="icon" viewBox="0 0 10 10"><path d="M2,1 L4,1 L5,3.5 L3.8,4.5 C4.4,5.8 5.2,6.6 6.5,7.2 L7.5,6 L10,7 L10,9 C5,9.5 0.5,5 1,1 Z" fill="#7d7d83"/></svg>(555) 014 2270</div>
        <div class="contact-item"><svg class="icon" viewBox="0 0 10 10"><rect x="1" y="3" width="8" height="6" fill="none" stroke="#7d7d83"/><rect x="3" y="1" width="4" height="3" fill="#7d7d83"/></svg>(555) 014 2271</div>
        <div class="contact-item"><svg class="icon" viewBox="0 0 10 10"><rect x="0.5" y="2" width="9" height="6" fill="none" stroke="#7d7d83"/><path d="M0.5,2 L5,5.5 L9.5,2" fill="none" stroke="#7d7d83"/></svg>care@lunaria-clinic.com</div>
      </div>
      <div>www.lunaria-clinic.com</div>
    </div>
  </section>

  <section class="piece card" aria-label="Business card">
    <svg class="wave" viewBox="0 0 100 30" preserveAspectRatio="none" aria-hidden="true">
      <path d="M0,0 H100 V4 C78,4 64,24 36,23 C20,22 8,17 0,15 Z" fill="url(#blush-band)"/>
      <path d="M0,15 C8,17 20,22 36,23 C64,24 78,4 100,4" fill="none" stroke="url(#silver-line)" stroke-width="1.6"/>
    </svg>
    <div class="brand"><span class="brand-dot"></span>Lunaria</div>
    <div class="card-person">
      <div class="card-name">MIRA</div>
      <div class="card-title">CEO / Founder</div>
    </div>
    <div class="card-contacts">
      <div class="contact-item"><svg class="icon" viewBox="0 0 10 10"><path d="M2,1 L4,1 L5,3.5 L3.8,4.5 C4.4,5.8 5.2,6.6 6.5,7.2 L7.5,6 L10,7 L10,9 C5,9.5 0.5,5 1,1 Z" fill="#7d7d83"/></svg>(555) 014 2270</div>
      <div class="contact-item"><svg class="icon" viewBox="0 0 10 10"><rect x="1" y="3" width="8" height="6" fill="none" stroke="#7d7d83"/><rect x="3" y="1" width="4" height="3" fill="#7d7d83"/></svg>(555) 014 2271</div>
      <div class="contact-item"><svg class="icon" viewBox="0 0 10 10"><rect x="0.5" y="2" width="9" height="6" fill="none" stroke="#7d7d83"/><path d="M0.5,2 L5,5.5 L9.5,2" fill="none" stroke="#7d7d83"/></svg>care@lunaria-clinic.com</div>
    </div>
    <div class="card-address">21 Ivory Lane<br>PO Box 415<br>Snowfield, NV 89010</div>
  </section>

  <section class="piece envelope" aria-label="Envelope">
    <svg class="wave" viewBox="0 0 100 30" preserveAspectRatio="none" aria-hidden="true">
      <path d="M0,0 H100 V6 C80,6 66,26 38,24 C22,23 9,16 0,13 Z" fill="url(#blush-band)"/>
      <path d="M0,13 C9,16 22,23 38,24 C66,26 80,6 100,6" fill="none" stroke="url(#silver-line)" stroke-width="1.6"/>
    </svg>
    <div class="brand"><span class="brand-dot"></span>Lunaria</div>
    <div class="contact-footer">
      <div>21 Ivory Lane<br>PO Box 415<br>Snowfield, NV 89010</div>
      <div>
        <div class="contact-item"><svg class="icon" viewBox="0 0 10 10"><path d="M2,1 L4,1 L5,3.5 L3.8,4.5 C4.4,5.8 5.2,6.6 6.5,7.2 L7.5,6 L10,7 L10,9 C5,9.5 0.5,5 1,1 Z" fill="#7d7d83"/></svg>(555) 014 2270</div>
        <div class="contact-item"><svg class="icon" viewBox="0 0 10 10"><rect x="1" y="3" width="8" height="6" fill="none" stroke="#7d7d83"/><rect x="3" y="1" width="4" height="3" fill="#7d7d83"/></svg>(555) 014 2271</div>
        <div class="contact-item"><svg class="icon" viewBox="0 0 10 10"><rect x="0.5" y="2" width="9" height="6" fill="none" stroke="#7d7d83"/><path d="M0.5,2 L5,5.5 L9.5,2" fill="none" stroke="#7d7d83"/></svg>care@lunaria-clinic.com</div>
      </div>
      <div>www.lunaria-clinic.com</div>
    </div>
  </section>
</main>
</body>
</html>
```